Design a Pre-Workout Package Design For a Supplement Company!

Create a colourful and energetic design for our pre-workout packaging! A small container that holds 30 servings of pre-workout needs to be designed to be eye-catching and inspirational! We want it to jump off the shelf into your face and scream positivity, energy and colour.

I've attached our logo- VEX Stamina which should be the face of the package with the colourful packaging behind it! Feel free to change it around! I've also attached a supplement company's pre-workout design that I love! Good luck!!!

Target Market(s)

Fitness goers

Industry/Entity Type

Fitness

Colors

Designer to choose colors to be used in the design.

Requirements
Must have
• -Logo-VEX Stamina on the front
• - Colourful, energetic, inspiration package

```html
<!DOCTYPE html>
<html lang="en">
<head>
<meta charset="UTF-8">
<title>VEX Stamina Pre-Workout Label</title>
<link href="https://fonts.googleapis.com/css2?family=Montserrat:wght@400;500;600&display=swap" rel="stylesheet">
<style>
  :root {
    --backdrop: #d3d3d3;
    --navy: #2a2a8a;
    --band: rgba(22, 30, 170, 0.78);
    --lime: #8fe01c;
    --white: #ffffff;
    --art-lime: #c8f01e;
    --art-cyan: #3fc4e8;
    --art-blue: #1a2fd0;
    --art-deep: #1b1690;
    --art-pink: #f07ac8;
    --art-red: #e8202a;
  }
  * { margin: 0; padding: 0; box-sizing: border-box; }
  html, body {
    width: 1200px;
    height: 1200px;
    overflow: hidden;
    background: var(--backdrop);
    font-family: "Montserrat", sans-serif;
  }
  .canvas {
    position: relative;
    width: 1200px;
    height: 1200px;
  }
  .label {
    position: absolute;
    left: 50px;
    top: 120px;
    width: 1100px;
    height: 960px;
    overflow: hidden;
  }
  .label-art {
    position: absolute;
    inset: 0;
    background:
      linear-gradient(100deg,
        var(--art-lime) 0%,
        var(--art-cyan) 14%,
        var(--art-blue) 30%,
        var(--art-deep) 46%,
        var(--art-pink) 58%,
        var(--art-blue) 70%,
        var(--art-lime) 84%,
        var(--art-red) 100%);
  }
  .servings-badge {
    position: absolute;
    left: 148px;
    top: 48px;
    width: 192px;
    height: 192px;
    border-radius: 50%;
    background: var(--navy);
    color: var(--lime);
    text-align: center;
    padding-top: 40px;
  }
  .servings-count {
    font-size: 76px;
    font-weight: 600;
    line-height: 1;
    letter-spacing: -2px;
  }
  .servings-word {
    font-size: 22px;
    font-weight: 400;
    margin-top: 4px;
  }
  .title-band {
    position: absolute;
    left: 0;
    right: 0;
    top: 700px;
    height: 200px;
    background: var(--band);
  }
  .brand-name {
    position: absolute;
    left: 60px;
    top: 64px;
    color: var(--white);
    font-size: 64px;
    font-weight: 600;
    letter-spacing: 1px;
    line-height: 1;
  }
  .product-info {
    position: absolute;
    left: 510px;
    top: 40px;
    color: var(--white);
  }
  .product-name {
    font-size: 64px;
    font-weight: 500;
    line-height: 1;
    letter-spacing: 1px;
  }
  .product-type {
    font-size: 24px;
    font-weight: 400;
    letter-spacing: 4px;
    margin-top: 14px;
  }
  .net-weight {
    font-size: 17px;
    font-weight: 500;
    margin-top: 12px;
    letter-spacing: 0.5px;
  }
</style>
</head>
<body>
  <main class="canvas">
    <section class="label">
      <div class="label-art" role="img" aria-label="Abstract fluid paint pour artwork in lime, cyan, royal blue, pink and red"></div>
      <div class="servings-badge">
        <div class="servings-count">30</div>
        <div class="servings-word">servings</div>
      </div>
      <div class="title-band">
        <div class="brand-name">VEX Stamina</div>
        <div class="product-info">
          <h1 class="product-name">PRE-WORKOUT</h1>
          <p class="product-type">DIETARY SUPPLEMENT</p>
          <p class="net-weight">NET WEIGHT:&nbsp; 594 LBS&nbsp; (270g)</p>
        </div>
      </div>
    </section>
  </main>
</body>
</html>
```